Cap supplier needs a newsletter design design

Looking for a new/fresh idea for an e-mail news letter.
My current newsletter can be found at the link below.
http://rondahats.net/newsletter_jan_2014/1a/index.html

The information needed does not change form the current newsletter.
Looking for a creative presentation with or without flash.

```html
<!DOCTYPE html>
<html lang="en">
<head>
<meta charset="utf-8">
<title>Ronda Hats International Newsletter</title>
<link rel="stylesheet" href="https://fonts.googleapis.com/css2?family=League+Gothic&family=Source+Sans+3:wght@400&display=swap">
<style>
:root{
  --page:#f1f1f1;
  --ink-dark:#1d1f26;
  --navy:#12275e;
  --navy-mid:#163070;
  --sky:#2aa9e6;
  --white:#ffffff;
  --muted:#6b6b6b;
  --link:#2a7fc9;
  --grey-head:#8a8a8a;
  --address-soft:#9fb0cf;
}
*{margin:0;padding:0;box-sizing:border-box}
html,body{width:820px;height:1200px;overflow:hidden;background:var(--page)}
body{position:relative;font-family:"League Gothic",sans-serif;color:var(--white)}
.utility{position:absolute;right:110px;font:400 9.5px "Source Sans 3",sans-serif;color:var(--muted);white-space:nowrap}
.utility a{color:var(--link);text-decoration:none;margin-left:4px}
.utility.top{top:57px}
.utility.bottom{top:1107px}
.sheet{position:absolute;left:102px;top:73px;width:617px;height:1032px;background:var(--white);box-shadow:0 0 2px rgba(0,0,0,.15)}
.band{position:absolute;left:0;width:617px;background:linear-gradient(180deg,var(--ink-dark) 0%,var(--navy) 100%);overflow:hidden}
.masthead{top:0;height:96px;text-align:center;white-space:nowrap}
.masthead h1{font-weight:400;font-size:45px;line-height:1;margin-top:20px}
.masthead p{font-size:17px;line-height:1;margin-top:1px}
.hero{position:absolute;top:96px;left:0;width:617px;height:397px}
.hero-collage{position:absolute;left:48px;top:4px;width:560px;height:384px;border-radius:40px;
  background:radial-gradient(ellipse 48% 30% at 46% 52%,#fff 55%,rgba(255,255,255,0) 100%),
  linear-gradient(135deg,#6e6a4a 0%,#1c1c24 30%,#2a3fb0 55%,#101010 75%,#2b3a8a 100%)}
.hero-text{position:absolute;left:0;top:0;width:617px;height:397px;font-weight:400;text-transform:uppercase;line-height:1;white-space:nowrap}
.hero-text span{position:absolute}
.hero-text .l1{left:215px;top:136px;font-size:44px;color:var(--navy);letter-spacing:1px}
.hero-text .which{left:236px;top:181px;font-size:25px;color:var(--grey-head)}
.hero-text .unique{left:305px;top:166px;font-size:60px;color:var(--sky)}
.hero-text .l3{left:283px;top:217px;font-size:42px;color:var(--navy-mid)}
.video{top:493px;height:98px}
.video h2{position:absolute;left:45px;top:16px;font-weight:400;font-size:44px;line-height:1;white-space:nowrap}
.video p{position:absolute;left:85px;top:58px;font-size:17px;line-height:1;white-space:nowrap}
.video svg{position:absolute;left:503px;top:7px}
.programs{position:absolute;top:613px;left:12px;width:594px;display:flex;gap:20px}
.program{width:184px;height:170px;border-radius:16px;overflow:hidden;background:var(--navy);box-shadow:0 1px 4px rgba(0,0,0,.35)}
.program header{height:60px;text-align:center;background:linear-gradient(180deg,#2a6f9a 0%,#1a3a5a 60%,#1a2438 100%);line-height:1;white-space:nowrap}
.program .kind{display:block;font-size:30px;color:var(--sky);padding-top:4px}
.program .word{display:block;font-size:29px;color:var(--white)}
.program p{font-size:19px;line-height:1.02;margin:20px 0 0 34px;width:145px}
.program .min{margin-top:20px}
.footer{top:819px;height:213px}
.footer-photo{position:absolute;left:248px;top:-22px;width:365px;height:215px;
  clip-path:polygon(56% 0,100% 0,100% 100%,0 100%,0 70%,35% 45%);
  background:linear-gradient(160deg,#c98a3a 0%,#6a4a2a 35%,#111 60%,#c88f20 100%)}
.footer .lead{position:absolute;left:12px;top:13px;font-size:18px;line-height:1;white-space:nowrap}
.footer .url{position:absolute;left:11px;top:30px;font-size:62px;line-height:1;color:var(--sky);white-space:nowrap}
.footer address{position:absolute;left:12px;top:122px;font-style:normal;font-size:14.5px;line-height:1.07;white-space:nowrap}
.footer address .name,.footer address .street{color:var(--address-soft)}
.footer address .mail{color:var(--sky)}
</style>
</head>
<body>
<p class="utility top">Can't see te images below?<a href="#">Click Here</a></p>
<main class="sheet">
  <section class="band masthead">
    <h1>RONDA HATS INTERNATIONAL</h1>
    <p>IMPORTED CUSTOM HEADWEAR</p>
  </section>
  <section class="hero">
    <div class="hero-collage" role="img" aria-label="Collage of embroidered custom baseball caps in camo, blue and black"></div>
    <h2 class="hero-text"><span class="l1">Design a cap</span><span class="which">which is</span><span class="unique">uniquely</span><span class="l3">yours !</span></h2>
  </section>
  <section class="band video">
    <h2>WATCH HOW AMAZINGLY EASY IT&nbsp; IS</h2>
    <p>SEE THE TWO MINUTE VIDEO EXPLAINING OUR SERVICE</p>
    <svg width="86" height="86" viewBox="0 0 86 86" aria-label="Play video"><circle cx="43" cy="43" r="39" fill="#2d3f78" stroke="#fff" stroke-width="4"/><path d="M32 24 L62 43 L32 62 Z" fill="#fff"/></svg>
  </section>
  <div class="programs">
    <article class="program"><header><span class="kind">CUSTOM</span><span class="word">PROGRAM</span></header><p>Design a cap which is uniquely yours</p><p class="min">150 caps minimum</p></article>
    <article class="program"><header><span class="kind">STANDARD</span><span class="word">PROGRAM</span></header><p>Custom , but the options are limited</p><p class="min">150 caps minimum</p></article>
    <article class="program"><header><span class="kind">KNIT HAT &amp; SCARF</span><span class="word">PROGRAM</span></header><p>Winter items with custom creativity</p><p class="min">150 caps minimum</p></article>
  </div>
  <footer class="band footer">
    <div class="footer-photo" role="img" aria-label="Cap printed with a tiger-stripe design"></div>
    <p class="lead">FOR MORE INFORMATION VISIT OUR WEBSITE</p>
    <p class="url">WWW.RONDAHATS.NET</p>
    <address>
      <span class="name">RONDA HATS INTERNATIONAL</span><br>
      <span class="street">2140 BIRCHMONT LANE, FAIRVIEW, VA, 22199</span><br>
      TELEPHONE&nbsp; 555-014-2871<br>
      FAX 555-014-2960<br>
      <span class="mail">INFO@RONDAHATS.NET</span>
    </address>
  </footer>
</main>
<p class="utility bottom">Want to unsubscribe from this newsletter ?<a href="#">Click Here</a></p>
</body>
</html>
```